Virtual assistant company needs letterhead and email signature

We need a letterhead and email signature for our virtual assistant company - dayBramble (small w capital F). Our tag line is think ahead | dayBramble

The colours we would like used are;

#81788c
#dddbe1

For reference our business cards have used #81788c background colour and #dddbe1 text

The fonts we would like used are

Lora
Proxima Nova

Please check out our twitter and facebook for style and feel

Twitter: @daybramble
www.chatterlane.com/daybramble

Please also find attached our landing page and business cards for reference

Any questions please let us know

Thanks
E

Reason: We like the opportunity to receive furthur designs

```html
<!DOCTYPE html>
<html lang="en">
<head>
<meta charset="utf-8">
<title>dayBramble email signature</title>
<link rel="stylesheet" href="https://fonts.googleapis.com/css2?family=Mulish:wght@400&family=Arimo:wght@400&display=swap">
<style>
  :root {
    --page: #f4f3f6;
    --ink: #222222;
    --brand: #81788c;
    --brand-light: #dddbe1;
    --brand-mid: #8f879a;
    --sign-ink: #3a3a3a;
  }
  * { margin: 0; padding: 0; box-sizing: border-box; }
  html, body {
    width: 1200px;
    height: 900px;
    overflow: hidden;
    background: var(--page);
  }
  .signature {
    position: absolute;
    left: 118px;
    top: 262px;
    width: 964px;
  }
  .signature__name {
    font-family: "Arimo", Arial, sans-serif;
    font-size: 26px;
    color: var(--ink);
    line-height: 1;
    margin-left: 2px;
  }
  .signature__handwriting {
    width: 240px;
    height: 90px;
    margin-top: 30px;
    background: linear-gradient(90deg, #5a5a5a 0%, #7a7a7a 100%);
    opacity: 0.6;
    border-radius: 4px;
  }
  .banner {
    position: relative;
    width: 964px;
    height: 196px;
    margin-top: 34px;
    background: linear-gradient(180deg, var(--brand-mid) 0%, var(--brand) 100%);
    color: var(--brand-light);
    font-family: "Mulish", Arial, sans-serif;
    font-weight: 400;
  }
  .banner__name {
    position: absolute;
    left: 36px;
    top: 40px;
    font-size: 52px;
    line-height: 1;
  }
  .banner__tagline {
    position: absolute;
    left: 38px;
    top: 128px;
    font-size: 24px;
    line-height: 1;
  }
  .banner__social {
    position: absolute;
    left: 536px;
    display: flex;
    align-items: center;
    font-size: 23px;
  }
  .banner__social--page { top: 36px; }
  .banner__social--handle { top: 106px; }
  .banner__dot {
    width: 52px;
    height: 52px;
    border-radius: 50%;
    background: var(--brand-light);
    margin-right: 14px;
  }
</style>
</head>
<body>
  <section class="signature">
    <p class="signature__name">Lorem ipsum</p>
    <div class="signature__handwriting" role="img" aria-label="Handwritten signature of the sender"></div>
    <div class="banner">
      <p class="banner__name">dayBramble</p>
      <p class="banner__tagline">think ahead | dayBramble</p>
      <p class="banner__social banner__social--page"><span class="banner__dot"></span>daybramble</p>
      <p class="banner__social banner__social--handle"><span class="banner__dot"></span>@daybramble</p>
    </div>
  </section>
</body>
</html>
```